Verdant Row

Currently www.verdantrow-example.com. This site was designed with a generic templet. However it is functional. I'm looking for a fun, fresh, and professional design. I also need help getting the XML for Searchly and Findo. I'm not a web designer and need help. I do not like my current sites narrow width.
Updates

All and all I'm liking the designs. The earlier ones seem better. Some seem that they are just taking my images and inputing them into a templet. I could have done that. The pictures are nice. Please keep in mind, functionality and updates. Please help us show our customers our how we are different. Safe Reliable Responsible are the key fundamentals, inside of these fundamentals show that were are customer service specialized. We are, Licensed, Insured, Drug Screened, Criminally Screened. Seems that people are putting up nice pictures but not capturing our values. Please help us market us on our website. Show our prospective customers why we are better, how we differentiate ourself from the competitors. Why choose us? Our flyers and cards are designed to drive our prospective customers to the website. If it looks identical with no pazaz like the card, then the marketing chain failed. I included our cards to help guide the thought process of our company. The link below is a feature I would love to have. This may be another project itself. I'm not sure if PX is the place to accomplish it. Below is a link for people to estimate there lawns with globe viewer. I would like to give a range of estimates using this technology. I have no clue how to accomplish it. If anyone knows how to who could do this, Please let me know. https://www.yardquoter-example.com/showOrder/MOWLAWN/propertyDetails

Target Market(s)

We target residential customers 30-80 yr old. We also are expanding and placing a special emphasis on Business accounts. The main service is a mowing and landscape maintenance. Should be the main focus of the site.

Industry/Entity Type

Searchly

Coding

Coded - Design and coding required

Font styles to use
Sans Serif

Requirements
Must have
• I want this site to be fun and colorful. It still needs to be professional looking as not to deter business accounts. If you use photos, they must reflect Florida lawn. Note the architecture the homes, grass type, types of plants.
Should not have
• My current site is ok. I use it just as a

```html
<!DOCTYPE html>
<html lang="en">
<head>
<meta charset="utf-8">
<title>Verdant Row — Lawn Care</title>
<link rel="stylesheet" href="https://fonts.googleapis.com/css2?family=Open+Sans:wght@400;600;700;800&display=swap">
<style>
  :root{
    --sky-top:#6fc0ec;
    --sky-bottom:#e4f4fc;
    --grass:#5bb52b;
    --grass-dark:#3f8f17;
    --quote-green:#3a7d10;
    --paper:#fbfbf7;
    --soil:#5a391b;
    --soil-dark:#47290f;
    --mint:#3cd27f;
    --mint-light:#5fe39a;
    --mint-card:#17a55a;
    --mint-deep:#21b464;
    --teal:#17718a;
    --leaf:#4da51c;
    --red:#e8412e;
    --btn-green:#34c87c;
    --bronze:#b8763a;
    --ink:#2f2f2f;
    --white:#ffffff;
    --nav-active:#5cc4e6;
  }
  *{box-sizing:border-box;margin:0;padding:0}
  html,body{width:1200px;height:2880px;overflow:hidden}
  body{font-family:"Open Sans",Arial,sans-serif;color:var(--ink);position:relative;background:var(--mint)}
  .abs{position:absolute}
  .section{position:absolute;left:0;width:1200px}

  /* hero */
  .hero{top:0;height:600px;background:linear-gradient(180deg,var(--sky-top) 0%,var(--sky-bottom) 85%)}
  .brand{left:48px;top:14px;width:300px}
  .brand-name{display:flex;align-items:center;gap:10px;font-weight:800;font-size:50px;color:var(--leaf);line-height:1}
  .brand-dot{width:30px;height:30px;border-radius:50%;background:var(--red)}
  .brand-web{font-weight:800;font-size:20px;color:#1d1d1d;margin-top:14px;letter-spacing:.3px}
  .brand-phone{font-weight:800;font-size:22px;color:#1d1d1d;margin-left:40px}
  .social-top{right:48px;top:18px;display:flex;gap:8px}
  .social-top span{width:24px;height:24px;border-radius:50%;background:var(--teal)}
  .nav{top:79px;left:547px;display:flex;gap:0;font-size:19px;color:#173a4a;text-transform:uppercase}
  .nav a{color:inherit;text-decoration:none;display:block;height:41px;line-height:41px;padding:0 17px}
  .nav a.active{background:var(--nav-active);color:var(--white)}
  .nav .about{margin-left:24px}
  .nav .services{margin-left:14px}
  .nav .estimate{margin-left:14px}
  .nav .contact{margin-left:14px}
  .tagline{left:44px;top:290px;line-height:1.1}
  .tagline .small{font-size:43px;color:var(--teal)}
  .tagline .big{font-size:49px;font-weight:800;color:var(--teal);margin:8px 0 6px;letter-spacing:.5px}
  .tagline .leaf{color:var(--leaf);font-weight:700}
  .btn{display:inline-block;color:var(--white);text-decoration:none;text-align:center;border-radius:3px}
  .btn-red{background:var(--red)}
  .reach{left:46px;top:504px;width:120px;height:41px;line-height:41px;font-size:21px}
  .sign-art{left:588px;top:120px;width:440px;height:450px;border-radius:14px;background:linear-gradient(160deg,#c08a55,#8c5a2c 55%,#6aa83a)}
  .mascot-art{left:1010px;top:450px;width:135px;height:130px;border-radius:40px;background:radial-gradient(circle at 50% 45%,#ef4b38,#c22b1d)}

  /* estimate band */
  .estimate{top:570px;height:340px;background:var(--grass)}
  .estimate h2{position:absolute;top:55px;width:100%;text-align:center;font-weight:400;font-size:46px;color:var(--white)}
  .estimate p{position:absolute;top:120px;width:100%;text-align:center;font-size:28px;color:var(--white)}
  .quote-form{position:absolute;left:221px;top:198px;width:768px;height:58px;display:flex}
  .quote-form .field{flex:1;background:var(--white);font-size:23px;color:#777;line-height:58px;padding-left:14px;border-radius:3px 0 0 3px}
  .quote-form .submit{width:279px;background:var(--quote-green);color:#b4f07a;font-size:23px;line-height:58px;text-align:center;border-radius:0 3px 3px 0}

  /* services */
  .services{top:900px;height:720px;background:var(--paper)}
  .section-title{position:absolute;width:100%;text-align:center;font-weight:400;font-size:46px}
  .services .section-title{top:22px;color:var(--bronze)}
  .arrows{position:absolute;right:48px;display:flex;gap:10px}
  .services .arrows{top:100px}
  .service{position:absolute;top:187px;width:260px;text-align:center}
  .service .photo{width:240px;height:240px;margin:0 auto;border-radius:50%;border:8px solid var(--bronze)}
  .service h3{font-weight:400;font-size:26px;line-height:31px;color:var(--ink);height:64px;margin-top:42px}
  .service .btn{background:var(--btn-green);width:134px;height:44px;line-height:44px;font-size:20px;margin-top:12px}

  /* about */
  .about-band{top:1596px;height:430px;background:var(--soil)}
  .roots-art{left:360px;top:1580px;width:480px;height:300px;border-radius:50%;background:radial-gradient(ellipse at 50% 20%,rgba(120,80,40,.55),rgba(90,57,27,0) 70%)}
  .about-mower{left:395px;top:1532px;width:250px;height:90px;border-radius:30px;background:linear-gradient(90deg,#e5402e 0 35%,#4bb02a 35% 100%)}
  .about-band h2{top:85px;color:var(--white)}
  .about-band p{position:absolute;left:72px;top:170px;width:1056px;text-align:center;font-size:23px;line-height:28px;color:var(--white)}
  .history{left:490px;top:1910px;width:214px;height:53px;line-height:53px;font-size:21px}

  /* feedback */
  .feedback{top:2004px;height:876px;background:linear-gradient(180deg,var(--mint) 0%,var(--mint-light) 100%)}
  .feedback .section-title{top:50px;color:var(--white)}
  .feedback .arrows{top:125px}
  .avatar{position:absolute;top:2196px;width:130px;height:130px;border-radius:50%;border:6px solid var(--white);background:linear-gradient(180deg,#d9e6ea,#9fb8c2)}
  .card{position:absolute;top:2304px;width:278px;height:216px;background:var(--mint-card);border-radius:3px;color:var(--white);padding:26px 20px 0 20px}
  .card .q{font-size:34px;font-weight:800;line-height:20px;height:20px}
  .card p{font-size:20px;line-height:24px;font-weight:600}
  .card .qr{position:absolute;right:18px;top:142px;font-size:34px;font-weight:800;line-height:20px}
  .card .who{position:absolute;right:18px;bottom:14px;font-size:18px;font-weight:700}

  /* footer */
  .footer-grass{left:0;top:2520px;width:1200px;height:260px;background:linear-gradient(180deg,rgba(47,183,101,0) 0%,var(--mint-deep) 45%,#26b060 100%)}
  .footer-brand{left:48px;top:2592px}
  .footer-brand .brand-name,.footer-brand .brand-web,.footer-brand .brand-phone{color:#1f7d45}
  .footer-brand .brand-name{font-size:44px}
  .footer-brand .brand-dot{background:#1f7d45}
  .social-foot{left:935px;top:2649px;display:flex;gap:20px}
  .social-foot span{width:42px;height:42px;border-radius:50%;background:var(--mint-light)}
  .footer-nav{left:660px;top:2790px;display:flex;gap:0;font-size:18px;text-transform:uppercase}
  .footer-nav a{color:#a9f1c6;text-decoration:none;margin-right:42px}
  .footer-nav a.active{color:var(--white)}
  .copyright{left:0;top:2854px;width:1200px;text-align:center;font-size:13px;color:var(--white)}
</style>
</head>
<body>

<header class="section hero">
  <div class="abs brand">
    <div class="brand-name"><span class="brand-dot"></span>Verdant Row</div>
    <div class="brand-web">WWW.VERDANTROW-EXAMPLE.COM</div>
    <div class="brand-phone">800-555-0142</div>
  </div>
  <div class="abs social-top"><span></span><span></span><span></span><span></span></div>
  <nav class="abs nav">
    <a class="active" href="#">Home</a>
    <a class="about" href="#">About</a>
    <a class="services" href="#">Services</a>
    <a class="estimate" href="#">Estimate</a>
    <a class="contact" href="#">Contact Us</a>
  </nav>
  <div class="abs tagline">
    <div class="small">We Put Our</div>
    <div class="big">PERSONALTOUCH</div>
    <div class="small">on <span class="leaf">Lawn Care</span></div>
  </div>
  <a class="abs btn btn-red reach" href="#">Reach us</a>
  <div class="abs sign-art" role="img" aria-label="Wooden signpost holding photos of a crew mowing and tending a lawn, set in tall grass"></div>
</header>

<section class="section estimate">
  <svg class="abs" style="left:0;top:-26px" width="1200" height="40" viewBox="0 0 1200 40" aria-hidden="true">
    <path d="M0 30 C150 5 300 35 450 18 C600 2 750 32 900 14 C1020 2 1110 22 1200 12 L1200 40 L0 40 Z" fill="#5bb52b"/>
  </svg>
  <h2>Schedule a free estimate today</h2>
  <p>It’s more affordable than you think.</p>
  <div class="quote-form">
    <div class="field">Enter Your Email ID</div>
    <div class="submit">Request for a free Quote</div>
  </div>
</section>
<div class="abs mascot-art" role="img" aria-label="Cartoon red lawn mower mascot peeking out of the grass"></div>

<section class="section services">
  <svg class="abs" style="left:0;top:-12px" width="1200" height="40" viewBox="0 0 1200 40" aria-hidden="true">
    <path d="M0 0 L1200 0 L1200 18 C1150 30 1120 8 1080 22 C1030 38 990 10 940 24 C880 36 850 8 800 20 C740 34 700 6 640 22 C580 36 540 10 480 24 C420 36 380 8 320 20 C260 34 220 6 160 22 C100 36 60 10 0 22 Z" fill="#5bb52b"/>
  </svg>
  <h2 class="section-title">Verdant Row Best Services</h2>
  <div class="arrows">
    <svg width="14" height="20" viewBox="0 0 14 20" aria-hidden="true"><path d="M11 2 L3 10 L11 18" stroke="#b8763a" stroke-width="2" fill="none"/></svg>
    <svg width="14" height="20" viewBox="0 0 14 20" aria-hidden="true"><path d="M3 2 L11 10 L3 18" stroke="#b8763a" stroke-width="2" fill="none"/></svg>
  </div>
  <div class="service" style="left:38px">
    <div class="photo" role="img" aria-label="Close-up of a red lawn mower on green grass" style="background:linear-gradient(135deg,#d9283a 0%,#b8222f 45%,#6fae3a 60%,#4e8f25 100%)"></div>
    <h3>Lawn Care</h3>
    <a class="btn" href="#">Find Details</a>
  </div>
  <div class="service" style="left:326px">
    <div class="photo" role="img" aria-label="Flower bed with pink blooms lining a garden path" style="background:linear-gradient(135deg,#5a9a2e 0%,#d9447a 40%,#e46fa0 60%,#4c8a26 100%)"></div>
    <h3>Flower Bed<br>Maintenance</h3>
    <a class="btn" href="#">Find Details</a>
  </div>
  <div class="service" style="left:614px">
    <div class="photo" role="img" aria-label="Gardener trimming a green hedge" style="background:linear-gradient(180deg,#b9d98a 0%,#6aa83a 50%,#3f7d1d 100%)"></div>
    <h3>Trimming<br>and Pruning</h3>
    <a class="btn" href="#">Find Details</a>
  </div>
  <div class="service" style="left:902px">
    <div class="photo" role="img" aria-label="Landscaped bed of shrubs and ornamental plants" style="background:linear-gradient(135deg,#7fb34a 0%,#c8553a 35%,#5e9a2c 60%,#3c7420 100%)"></div>
    <h3>Plant and Shrub<br>Installation</h3>
    <a class="btn" href="#">Find Details</a>
  </div>
</section>

<section class="section about-band">
  <svg class="abs" style="left:0;top:-20px" width="1200" height="40" viewBox="0 0 1200 40" aria-hidden="true">
    <path d="M0 20 C120 8 220 28 360 18 C500 8 620 30 760 16 C900 4 1040 26 1200 14 L1200 40 L0 40 Z" fill="#5a391b"/>
  </svg>
  <h2 class="section-title">Who We Are</h2>
  <p>Lorem ipsum dolor sit amet, consectetuer adipiscing elit, sed diam nonummy nibh euismod tincidunt ut laoreet dolore magna aliquam erat volutpat. Ut wisi enim ad minim veniam, quis nostrud exerci tation ullamcorper suscipit lobortis nisl ut aliquip ex ea commodo consequat.</p>
  <svg class="abs" style="left:0;top:404px" width="1200" height="40" viewBox="0 0 1200 40" aria-hidden="true">
    <path d="M0 10 C60 30 120 0 200 18 C280 34 340 4 420 20 C500 34 560 6 640 20 C720 34 800 4 880 18 C960 32 1040 6 1120 20 C1160 28 1180 18 1200 14 L1200 40 L0 40 Z" fill="#3cd27f"/>
  </svg>
</section>
<div class="abs roots-art" role="img" aria-label="Faint plant roots spreading through the soil"></div>
<div class="abs about-mower" role="img" aria-label="Cartoon red mower mascot beside a tuft of grass"></div>
<a class="abs btn btn-red history" href="#">Find Our History</a>

<section class="section feedback">
  <h2 class="section-title">Client’s Feedback</h2>
  <div class="arrows">
    <svg width="14" height="20" viewBox="0 0 14 20" aria-hidden="true"><path d="M11 2 L3 10 L11 18" stroke="#7fe9ad" stroke-width="2" fill="none"/></svg>
    <svg width="14" height="20" viewBox="0 0 14 20" aria-hidden="true"><path d="M3 2 L11 10 L3 18" stroke="#7fe9ad" stroke-width="2" fill="none"/></svg>
  </div>
</section>

<div class="abs avatar" style="left:158px" role="img" aria-label="Portrait of client Marlene"></div>
<div class="abs avatar" style="left:533px" role="img" aria-label="Portrait of client Theo"></div>
<div class="abs avatar" style="left:912px" role="img" aria-label="Portrait of client Priya"></div>

<article class="card" style="left:84px">
  <div class="q">“</div>
  <p>Lorem ipsum dolor sit amet, consectetuer adipiscing elit, sed diam nonummy nibh euismod tincidunt ut</p>
  <div class="qr">”</div>
  <div class="who">Marlene</div>
</article>
<article class="card" style="left:459px">
  <div class="q">“</div>
  <p>Lorem ipsum dolor sit amet, consectetuer adipiscing elit, sed diam nonummy nibh euismod tincidunt ut</p>
  <div class="qr">”</div>
  <div class="who">Theo</div>
</article>
<article class="card" style="left:836px">
  <div class="q">“</div>
  <p>Lorem ipsum dolor sit amet, consectetuer adipiscing elit, sed diam nonummy nibh euismod tincidunt ut</p>
  <div class="qr">”</div>
  <div class="who">Priya</div>
</article>

<footer>
  <div class="abs footer-grass" role="img" aria-label="Silhouette of tall grass blades along the bottom of the page"></div>
  <div class="abs footer-brand">
    <div class="brand-name"><span class="brand-dot"></span>Verdant Row</div>
    <div class="brand-web">WWW.VERDANTROW-EXAMPLE.COM</div>
    <div class="brand-phone">800-555-0142</div>
  </div>
  <div class="abs social-foot"><span></span><span></span><span></span><span></span></div>
  <nav class="abs footer-nav">
    <a class="active" href="#">Home</a>
    <a href="#">About</a>
    <a href="#">Services</a>
    <a href="#">Estimate</a>
    <a href="#">Contact Us</a>
  </nav>
  <div class="abs copyright">Copyright Verdant Row 2014. All Rights Reserved.</div>
</footer>

</body>
</html>
```